Healthy Food Healthy Brain Rack Card

We want a new 2 page (front and page) 3.67" x 8.5" rack card. This rack card is the first of a series we are creating. We will have five more eventually.

The minimum font size for the text on the front is 11 point and also for other main body text.

Use the text on the word document.

The images and layout in the word document are just sample ideas we had.

We have a subscripton to pelvane stock images so prefer to get images from there or free high quality images.

The document is for older readers. Do not put text over graphics and keep it simple and easy to read with high contrast.

We are open to any color scheme, though something that conveys fresh and healthy, is good.

We want some very simple design element(s) incorporated that convey Native American communities or heritage. But NO head dress, teepee graphics, etc.

At the top, of the first page we would like a collage of healthy food images. This can include fish, chicken, fresh vegetables, berries, brown rice, etc.

On the back side, the text below the brown box on the word document with the title "mock up" can be smaller as needed.

Please remember to include the funding statement - it can be in a very small font 6/7 point.

For more information about our project, please visit https://morvetlin.org/brain-health/

```html
<!DOCTYPE html>
<html lang="en">
<head>
<meta charset="utf-8">
<title>Healthy Food Healthy Brain Rack Card</title>
<link href="https://fonts.googleapis.com/css2?family=Poppins:ital,wght@0,400;0,500;0,600;0,700;1,400;1,500;1,600&display=swap" rel="stylesheet">
<style>
  :root {
    --green: #4b9140;
    --ink: #6b6b6b;
    --ink-strong: #555555;
    --backdrop: #2c2e2e;
    --white: #ffffff;
    --teal: #5ba6ad;
  }
  * { box-sizing: border-box; margin: 0; padding: 0; }
  html, body { width: 1200px; height: 1019px; overflow: hidden; }
  body {
    background: var(--backdrop);
    font-family: "Poppins", sans-serif;
    color: var(--ink);
    position: relative;
  }
  .card {
    position: absolute;
    top: 80px;
    width: 371px;
    height: 859px;
    background: linear-gradient(120deg, #f4f4f4 0%, #eeeeee 40%, #f5f5f5 60%, #efefef 100%);
    overflow: hidden;
  }
  .card--front { left: 199px; }
  .card--back { left: 630px; }

  /* Front */
  .food-collage {
    position: absolute; left: 0; top: 0; width: 371px; height: 294px;
    background: linear-gradient(135deg, #4a4038 0%, #7d8a3a 30%, #c9b48a 55%, #8c2f4a 75%, #5f8a3a 100%);
    clip-path: polygon(0 0, 100% 0, 100% 284px, 0 294px);
  }
  .front-title {
    position: absolute; left: 0; width: 100%; top: 291px;
    text-align: center; color: var(--green);
    font-weight: 500; font-size: 41px; line-height: 41px; letter-spacing: -0.3px;
  }
  .front-title__box {
    position: absolute; left: 40px; top: 336px; width: 291px; height: 36px;
    background: var(--green); color: var(--white);
    font-weight: 700; font-size: 36px; line-height: 37px; text-align: center; letter-spacing: -0.4px;
    white-space: nowrap;
  }
  .front-text {
    position: absolute; left: 40px; width: 292px;
    font-size: 12.7px; line-height: 15.2px; letter-spacing: -0.1px;
  }
  .front-text--intro { top: 380px; text-align: justify; }
  .front-text--lead { top: 474px; }
  .front-text--closing { top: 756px; left: 44px; width: 288px; }
  .steps { list-style: none; position: absolute; left: 40px; top: 496px; width: 292px;
    font-size: 12.7px; line-height: 15.3px; letter-spacing: -0.1px; }
  .steps li { position: relative; padding-left: 21px; margin-bottom: 3px; }
  .steps li::before {
    content: ""; position: absolute; left: 6px; top: 6px;
    width: 3px; height: 3px; border-radius: 50%; background: var(--green);
  }
  .band {
    position: absolute; left: 0; top: 795px; width: 100%; height: 64px;
    background: var(--green); color: var(--white);
    display: flex; align-items: center; justify-content: center; text-align: center;
  }
  .band--cta { font-weight: 700; font-size: 15px; line-height: 19px; padding: 0 20px; }

  /* Back */
  .back-title {
    position: absolute; left: 22px; top: 10px;
    color: var(--green); font-weight: 500; font-size: 40px; line-height: 40px; letter-spacing: 0.5px;
    white-space: nowrap;
  }
  .back-title__box {
    position: absolute; left: 22px; top: 57px; width: 149px; height: 42px;
    background: var(--green); color: var(--white);
    font-weight: 700; font-size: 42px; line-height: 45px; text-align: center;
  }
  .recipe-name {
    position: absolute; left: 22px; top: 110px; width: 150px;
    color: var(--green); font-style: italic; font-weight: 500; font-size: 10.8px; line-height: 15px;
  }
  .recipe-photo {
    position: absolute; left: 21px; top: 149px; width: 147px; height: 124px;
    background: radial-gradient(circle at 55% 60%, #e8673e 0%, #c84b2c 25%, #3e4a2e 60%, #1f2520 100%);
  }
  .ingredients {
    position: absolute; left: 183px; top: 62px; width: 186px;
    list-style: none; font-size: 12.6px; line-height: 19.6px; white-space: nowrap;
  }
  .ingredients .label { font-weight: 600; }
  .ingredients .note { font-style: italic; font-size: 11.8px; }
  .method {
    position: absolute; left: 21px; top: 287px; width: 331px;
    font-size: 12.7px; line-height: 15.1px; letter-spacing: -0.1px;
  }
  .heritage-note {
    position: absolute; left: 21px; top: 421px; width: 329px; height: 98px;
    border: 1px solid var(--green);
    color: var(--green); font-style: italic; font-weight: 500; font-size: 12.8px; line-height: 18.2px;
    text-align: center; display: flex; align-items: center; justify-content: center; padding: 0 18px;
  }
  .info-line { position: absolute; left: 0; width: 100%; text-align: center; white-space: nowrap; }
  .info-heading { top: 529px; color: var(--green); font-weight: 600; font-size: 17px; line-height: 22px; }
  .info-topic { color: var(--ink-strong); font-weight: 600; font-size: 11.2px; line-height: 16px; }
  .info-topic--eating { top: 549px; }
  .info-topic--brain { top: 611px; }
  .info-org { color: var(--green); font-weight: 600; font-size: 11.5px; line-height: 14px; }
  .info-org--plate { top: 569px; font-weight: 500; }
  .info-org--center { top: 631px; }
  .info-org--aging { top: 688px; }
  .info-url { color: var(--ink-strong); font-size: 11px; line-height: 16px; letter-spacing: 2.6px; }
  .info-url--plate { top: 586px; }
  .info-url--center { top: 663px; }
  .info-url--aging { top: 706px; }
  .org-sign {
    position: absolute; left: 90px; top: 740px; height: 50px;
    display: flex; align-items: center; gap: 10px;
  }
  .org-sign__dot { width: 48px; height: 48px; border-radius: 50%; background: var(--teal); }
  .org-sign__name { color: var(--teal); font-weight: 500; font-size: 15px; line-height: 1; }
  .band--funding { font-size: 5.6px; line-height: 8.6px; padding: 0 16px; }
</style>
</head>
<body>

<section class="card card--front">
  <div class="food-collage" role="img" aria-label="Collage of healthy foods: grilled fish, roast chicken, green salad, fresh berries, brown rice and greens"></div>
  <h1 class="front-title">HEALTHY FOOD</h1>
  <div class="front-title__box">HEALTHY BRAIN</div>
  <p class="front-text front-text--intro">Everyone slows down as they get older, both in body and mind. Eating healthier food can help your overall health, including brain health. It may also reduce your risk for memory loss and problems thinking</p>
  <p class="front-text front-text--lead">Healthier steps to protect your brain:</p>
  <ul class="steps">
    <li>Eat more vegetables, fruits, whole grains, and lower-fat milk</li>
    <li>Use less salt and added sugar</li>
    <li>Eat more fish, chicken, turkey, beans, and nuts</li>
    <li>Cut down on bad fats (“saturated” and trans), cholesterol, and red meat</li>
    <li>Buy fresh, not packaged food when you can</li>
    <li>Limit how much alcohol you drink</li>
    <li>Learn your daily calorie needs for your body size</li>
    <li>Take care of your mental and spiritual health to support your physical and brain health</li>
  </ul>
  <p class="front-text front-text--closing">Small changes can make a big difference for better brain health.</p>
  <div class="band band--cta">Talk to your doctor about more steps to healthier food choices.</div>
</section>

<section class="card card--back">
  <h2 class="back-title">MAKE THIS AT</h2>
  <div class="back-title__box">HOME</div>
  <p class="recipe-name">Grilled Salmon and Veggie Foil Packets</p>
  <div class="recipe-photo" role="img" aria-label="Raw salmon fillet with herbs, tomatoes and sea salt"></div>
  <ul class="ingredients">
    <li class="label">Ngredients:</li>
    <li>Salmon</li>
    <li>Asparagus</li>
    <li>Red or Green Peppers</li>
    <li class="note">(Or any seasonal vegetable)</li>
    <li>Onion</li>
    <li>Lemon – sliced</li>
    <li>Basil</li>
    <li>Olive Oil</li>
    <li>Salt and Pepper</li>
    <li>Garlic Powder</li>
  </ul>
  <p class="method">Cut asparagus, peppers, and onion into bite-size pieces. Cut salmon into 4-6 oz pieces. Tear tin foil large enough to wrap around salmon &amp; veggies (2 layers). Add veggies and salmon to foil. Drizzle with olive oil, season with salt, pepper, basil, garlic &amp; top with a piece of sliced lemon. Wrap foil tightly around food. Grill at 400 degrees for about 20 minutes. Careful opening!</p>
  <div class="heritage-note">Food &amp; drink are a source of strength and connectio to community. A return to traditional food pathways and eating local seasonal fresh foods make healthier eating easier.</div>

  <h2 class="info-line info-heading">For More Information</h2>
  <h3 class="info-line info-topic info-topic--eating">About Healthier Eating</h3>
  <p class="info-line info-org info-org--plate">PlateWise</p>
  <p class="info-line info-url info-url--plate">www.platewiseguide.org</p>
  <h3 class="info-line info-topic info-topic--brain">About Brain Health</h3>
  <p class="info-line info-org info-org--center">Kestrel Ridge Center for<br>Native Brain Health</p>
  <p class="info-line info-url info-url--center">www.KestrelBrainHealth.org</p>
  <p class="info-line info-org info-org--aging">Corvane Healthy Aging Program</p>
  <p class="info-line info-url info-url--aging">www.corvane.org/aging</p>

  <div class="org-sign">
    <span class="org-sign__dot"></span>
    <span class="org-sign__name">Kestrel Ridge Center</span>
  </div>
  <div class="band band--funding">This product is supported by the Corvane Health Foundation as part of a financial assistance award totaling $348,711 with 100 percent funded by Corvane. The contents are those of the author(s) and do not necessarily represent the official views of, nor an endorsement by, Corvane.</div>
</section>

</body>
</html>
```